Wordpress - For IT, Cloud/Hosting, Residential/Commercial Construction Services

We are a holding company for service companies. We want the current Wordpress site modified or a new wordpress site completed. We want this site to be the parent website, that then has pull down menus linking to our other website (currently http://quarnelworks.com, http://n4cq.host and would like it to be easy and fluid as we acquire more companies as we have with TLKZ, Inc., V&V Construction, Quarnel Works etc. Model after sites like Zindle.com, Brovantic.com, KTQ.com,.ferncastle.com

------

The parent is the main site n4c Corp. Below that are sub corps and DBAs. n4c Corp stands for Near 4 Care Corp. n4c Offers IT manages services, 24x7 support, Monitoring NOC, Remote Hands, Onsite support services. We have acquired TLKZ, Inc, V & V Construction, QuarnelWorks.com. We plan to acquire/spin up many companies that offer service, support and installation offerings and will all be known as an n4c Corp Company for branding purposes. We recently had our logo done, but then ran it through 3d glass as we like the look better than the original works. We have original files in vector, but not the 3D galss door render.

Target Market(s)

IT Server and Desktop Support. Construction. Mold Remediation. Mergers and Acquisitions.

Industry/Entity Type

It Company

Coding

Coded - Design and coding required

Font styles to use
Sans Serif

Colors
0792cd

Requirements
Must have
• Clean interface. Modern design. Mobile device and multi browser support. Must be for Wordpress. Job posting with resume submission module.Hook to our Web hosting portal (Vurdo) API into TrelBix Reseller portal, customer portal to allow payments to their account etc.. Easy to edit. Easy to add to, Press Release Section, Investor Relations etc.
Should not have
• Slow loading. Played out design. Over use of stock images. Copied from a competitor or something point to such.

```html
<!DOCTYPE html>
<html lang="en">
<head>
<meta charset="utf-8">
<title>n4c Corp — Holding company for service companies</title>
<link rel="stylesheet" href="https://fonts.googleapis.com/css2?family=Roboto:wght@300;400;500;700&family=Open+Sans:wght@400;600&display=swap">
<style>
:root{
  --blue:#1f73c1;
  --blue-dark:#1862a8;
  --ink:#222;
  --text:#555;
  --muted:#888;
  --line:#e3e3e3;
  --footer:#2b2b2b;
  --footer-bottom:#1f1f1f;
  --field:#3b3b3b;
  --white:#fff;
}
*{box-sizing:border-box;margin:0;padding:0}
html,body{width:1200px;height:3504px;overflow:hidden}
body{font-family:"Open Sans",sans-serif;color:var(--text);background:var(--white);font-size:14px}
.wrap{width:860px;margin:0 auto;position:relative}
h1,h2,h3,h4{font-family:"Roboto",sans-serif;font-weight:400;color:var(--ink)}
.section-title{font-size:30px;text-align:center;position:relative;padding-bottom:18px}
.section-title::after{content:"";position:absolute;left:50%;bottom:0;width:50px;height:2px;margin-left:-25px;background:var(--blue)}
.section-title.light{color:var(--white)}
.section-title.light::after{background:rgba(255,255,255,.6)}

/* top bar */
.topbar{height:30px;background:var(--blue);color:var(--white);font-size:11px}
.topbar .wrap{display:flex;justify-content:space-between;align-items:center;height:30px}
.topbar .info,.topbar .account{display:flex;gap:22px;align-items:center}
.topbar .dot{display:inline-block;width:8px;height:8px;border-radius:50%;background:var(--white);margin-right:6px;vertical-align:-1px}
.social{display:flex;gap:8px}
.social span{width:10px;height:10px;border-radius:50%;background:rgba(255,255,255,.85)}

/* header */
.header{height:92px;border-bottom:1px solid var(--line)}
.header .wrap{height:92px}
.brand{position:absolute;left:0;top:16px;font-family:"Roboto",sans-serif;font-weight:700;font-size:30px;color:var(--blue);display:flex;align-items:center;gap:10px}
.brand i{width:22px;height:22px;background:var(--blue);border-radius:50%}
.acquired-select{position:absolute;right:0;top:14px;display:flex;align-items:center;gap:10px;font-size:12px;color:var(--ink)}
.acquired-select span.box{width:130px;height:22px;border:1px solid #ccc;border-radius:3px;font-size:10px;color:var(--muted);padding:3px 8px}
.nav{position:absolute;right:0;top:60px;display:flex;gap:26px;font-family:"Roboto",sans-serif;font-size:13px;color:var(--ink)}

/* hero */
.hero{height:453px;position:relative;background:linear-gradient(180deg,#3a4049 0%,#24292f 55%,#3c4148 100%);text-align:center;color:var(--white)}
.hero h1{color:var(--white);font-weight:300;font-size:62px;line-height:74px;padding-top:112px}
.btn{display:inline-block;background:var(--blue);color:var(--white);font-family:"Roboto",sans-serif;font-size:14px;border-radius:3px}
.hero .btn{margin-top:38px;width:206px;height:40px;line-height:40px;border-radius:20px;font-size:16px}
.hero-arrow{position:absolute;top:206px;width:34px;height:42px;background:rgba(200,200,200,.75);display:flex;align-items:center;justify-content:center}
.hero-arrow.prev{left:30px}.hero-arrow.next{right:30px}

/* story */
.story{height:505px;padding-top:90px}
.story h2{font-size:30px;position:relative;padding-bottom:18px}
.story h2::after{content:"";position:absolute;left:0;bottom:0;width:50px;height:2px;background:var(--blue)}
.story .cols{display:flex;justify-content:space-between;margin-top:44px}
.story .copy{width:400px;font-size:13.5px;line-height:22px}
.story .copy p{margin-bottom:20px}
.story .video{width:418px;height:200px;background:linear-gradient(135deg,#c9ccd1,#8c939c);position:relative;display:flex;align-items:center;justify-content:center}

/* why choose */
.why{height:350px;background:var(--blue);padding-top:64px}
.features{display:flex;justify-content:space-between;margin-top:60px;padding:0 6px}
.feature{width:160px;text-align:center;color:var(--white);font-family:"Roboto",sans-serif;font-size:15px}
.feature svg{display:block;margin:0 auto 20px}

/* acquired */
.acquired{height:580px;padding-top:70px}
.acquired .slide{display:flex;margin-top:60px;gap:30px}
.acquired .visual{width:404px;height:350px;background:linear-gradient(180deg,#e9eaec,#d7d9dc)}
.acquired .detail{width:418px;padding-top:46px;position:relative;height:350px}
.acquired h3{font-size:20px;font-weight:700;margin-bottom:20px}
.acquired p{font-size:13px;line-height:21px}
.acquired .btn{margin-top:28px;padding:8px 20px;font-size:13px}
.acquired .company-mark{position:absolute;right:0;bottom:36px;font-family:"Roboto",sans-serif;font-weight:700;font-size:22px;color:var(--ink)}
.slide-arrow{position:absolute;top:295px;width:36px;height:38px;background:var(--blue);display:flex;align-items:center;justify-content:center}
.slide-arrow.prev{left:-70px}.slide-arrow.next{right:-70px}

/* testimonials */
.testimonials{height:457px;background:var(--blue);padding-top:50px;text-align:center;color:var(--white)}
.avatars{display:flex;justify-content:center;gap:14px;margin-top:44px}
.avatars span{width:68px;height:68px;border-radius:50%;border:3px solid var(--white);background:linear-gradient(180deg,#d8c3b0,#8f7b6d)}
.quote-mark{margin:28px auto 14px;display:block}
.testimonials blockquote{width:700px;margin:0 auto;font-size:13.5px;line-height:21px}
.testimonials cite{display:block;margin-top:30px;font-style:normal;font-size:13px}
.testimonials cite::before{content:"";display:inline-block;width:60px;height:1px;background:var(--white);vertical-align:middle;margin-right:8px}

/* news */
.news{height:483px;padding-top:68px}
.news-grid{display:flex;gap:25px;margin-top:60px}
.card{width:270px;height:310px;border:1px solid var(--line)}
.card .photo{height:200px;position:relative}
.card .photo .go{position:absolute;right:8px;bottom:8px;width:32px;height:30px;background:var(--blue);display:flex;align-items:center;justify-content:center}
.card .body{padding:10px 12px}
.card h4{font-size:16px;font-weight:500}
.card .meta{font-size:10px;color:var(--muted);margin:6px 0;display:flex;gap:16px}
.card p{font-size:11.5px;line-height:16px}

/* clients */
.clients{height:175px}
.clients .wrap{display:flex;justify-content:space-between;align-items:center;height:175px;padding:0 10px}
.clients span{font-family:"Roboto",sans-serif;font-size:34px;font-weight:400;color:#8a8a8a}

/* footer */
.footer{height:350px;background:var(--footer);color:#cfcfcf;padding-top:50px;font-size:12.5px}
.footer .wrap{display:flex;gap:0}
.footer .col{width:293px}
.footer h4{color:var(--white);font-size:15px;font-weight:500;padding-bottom:10px;border-bottom:1px solid #555;margin-bottom:20px;width:270px}
.contact-list li{list-style:none;display:flex;gap:12px;margin-bottom:16px;align-items:center}
.contact-list svg{flex:none}
.footer .social{margin-top:6px;gap:14px}
.footer .social span{background:#bbb}
.field{width:270px;height:28px;background:var(--field);margin-bottom:8px;font-size:10px;color:#999;padding:7px 8px}
.field.area{height:76px}
.footer .btn{width:270px;height:28px;line-height:28px;text-align:center;font-size:12px;border-radius:0}
.bottombar{height:29px;background:var(--footer-bottom);color:#888;font-size:10px}
.bottombar .wrap{line-height:29px}
</style>
</head>
<body>

<header>
  <div class="topbar">
    <div class="wrap">
      <div class="info">
        <span><i class="dot"></i>info@n4c.com</span>
        <span><i class="dot"></i>000-0000-0000</span>
        <span><i class="dot"></i>12, nam soluta nobis est eligendi</span>
      </div>
      <div class="account">
        <span><i class="dot"></i>Login/Signup</span>
        <div class="social"><span></span><span></span><span></span><span></span></div>
      </div>
    </div>
  </div>
  <div class="header">
    <div class="wrap">
      <div class="brand"><i></i>n4c Corp</div>
      <div class="acquired-select">Acquired <span class="box">Select...</span></div>
      <nav class="nav"><span>Home</span><span>About Us</span><span>Services</span><span>Testimonials</span><span>Our Blog</span><span>Contact Us</span></nav>
    </div>
  </div>
</header>

<section class="hero" role="img" aria-label="Dark city skyline of glass office towers">
  <h1>We are a holding company<br>for service companies</h1>
  <span class="btn">Learn More</span>
  <span class="hero-arrow prev"><svg width="12" height="16" viewBox="0 0 12 16"><path d="M9 2 3 8l6 6" fill="none" stroke="#333" stroke-width="2.5"/></svg></span>
  <span class="hero-arrow next"><svg width="12" height="16" viewBox="0 0 12 16"><path d="M3 2l6 6-6 6" fill="none" stroke="#333" stroke-width="2.5"/></svg></span>
</section>

<section class="story">
  <div class="wrap">
    <h2>Our Story</h2>
    <div class="cols">
      <div class="copy">
        <p>n4c Corp is a Dralvex and Brovantic Solution Provider. We provide support for Desktops, Laptops, Tablets, Mobile Devices, Networking, Wifi, Server, Design and more by providing Remote and Onsite Support Services.</p>
        <p>n4c Corp ( Near 4 Care ) Full service one-stop shop service provider. Our CEO and Founder Pell Arrowby has been working with Brovantic Solutions all the way back to early DOS and all the way to Brovantic's solution offerings of today. We trains his team to be clones of his highly technical mindset of "can do it all aptitude" because he feels nothing in technology is cut and dry, as each client and each technology work uniquely!</p>
        <p>n4c is a Dralvex and Brovantic Solution partner.</p>
      </div>
      <div class="video" role="img" aria-label="Video still of a smiling business team in an office">
        <svg width="60" height="42" viewBox="0 0 60 42"><rect width="60" height="42" rx="10" fill="#1f73c1"/><path d="M24 12l14 9-14 9z" fill="#fff"/></svg>
      </div>
    </div>
  </div>
</section>

<section class="why">
  <div class="wrap">
    <h2 class="section-title light">Why Choose Us</h2>
    <div class="features">
      <div class="feature">
        <svg width="60" height="60" viewBox="0 0 60 60" fill="none" stroke="#fff" stroke-width="2.5"><path d="M12 48 40 20M36 10a10 10 0 0 0 14 14l-6-2-6-6z"/><path d="M12 12l8 8m20 20 8 8M10 20l10-10"/></svg>
        IT Manages Services
      </div>
      <div class="feature">
        <svg width="60" height="60" viewBox="0 0 60 60" fill="none" stroke="#fff" stroke-width="2.5"><circle cx="30" cy="30" r="22"/><text x="30" y="36" fill="#fff" stroke="none" font-size="16" font-family="Roboto,sans-serif" text-anchor="middle">24</text></svg>
        24x7 Support
      </div>
      <div class="feature">
        <svg width="60" height="60" viewBox="0 0 60 60" fill="none" stroke="#fff" stroke-width="2.5"><rect x="22" y="6" width="16" height="12"/><rect x="6" y="42" width="14" height="11"/><rect x="23" y="42" width="14" height="11"/><rect x="40" y="42" width="14" height="11"/><path d="M30 18v10M13 42V32h34v10M30 28v14"/></svg>
        Monitoring NOC
      </div>
      <div class="feature">
        <svg width="60" height="60" viewBox="0 0 60 60" fill="none" stroke="#fff" stroke-width="2.5"><rect x="22" y="6" width="16" height="30" rx="3"/><path d="M18 54V36l-4-6m24 24V40l8-6"/></svg>
        Remote Hands
      </div>
      <div class="feature">
        <svg width="60" height="60" viewBox="0 0 60 60" fill="none" stroke="#fff" stroke-width="2.5"><rect x="8" y="12" width="44" height="30" rx="2"/><path d="M22 50h16M30 42v8M18 34l8-8 6 5 10-10"/></svg>
        Onsite Support
      </div>
    </div>
  </div>
</section>

<section class="acquired">
  <div class="wrap">
    <h2 class="section-title">We have Acquired</h2>
    <div class="slide">
      <div class="visual" role="img" aria-label="Illustration of construction tools: hard hat, drill, hammer and gloves"></div>
      <div class="detail">
        <h3>V&amp;V Construction</h3>
        <p>Vellard &amp; Vellard handles diverse projects, encompassing a broad range of services, for both public and private sector. Many of our projects are either commercial, design/build or multi family services. And all of it supported by nearly 25 years experience in the industry working for public agencies, municipalities, commercial developers, architects and engineers, the military, and private developers.</p>
        <span class="btn">Read More</span>
        <span class="company-mark">V&amp;V Construction</span>
      </div>
    </div>
    <span class="slide-arrow prev"><svg width="12" height="16" viewBox="0 0 12 16"><path d="M9 2 3 8l6 6" fill="none" stroke="#fff" stroke-width="2.5"/></svg></span>
    <span class="slide-arrow next"><svg width="12" height="16" viewBox="0 0 12 16"><path d="M3 2l6 6-6 6" fill="none" stroke="#fff" stroke-width="2.5"/></svg></span>
  </div>
</section>

<section class="testimonials">
  <h2 class="section-title light">Testimonials</h2>
  <div class="avatars">
    <span role="img" aria-label="Client portrait"></span><span role="img" aria-label="Client portrait"></span><span role="img" aria-label="Client portrait"></span><span role="img" aria-label="Client portrait"></span><span role="img" aria-label="Client portrait"></span><span role="img" aria-label="Client portrait"></span>
  </div>
  <svg class="quote-mark" width="34" height="28" viewBox="0 0 34 28" fill="#fff"><path d="M2 28V16C2 7 6 2 14 0l1 4c-4 2-6 5-6 9h6v15zm18 0V16c0-9 4-14 12-16l1 4c-4 2-6 5-6 9h6v15z"/></svg>
  <blockquote>Duis aute irure dolor in reprehenderit in voluptate velit esse cillum dolore eu fugiat nulla pariatur. Excepteur sint occaecat cupidatat non proident, sunt in culpa qui officia deserunt mollit anim id est laborum.</blockquote>
  <cite>Aldric Venn</cite>
</section>

<section class="news">
  <div class="wrap">
    <h2 class="section-title">Latest News</h2>
    <div class="news-grid">
      <article class="card">
        <div class="photo" role="img" aria-label="Technician working in a server room" style="background:linear-gradient(135deg,#4a5a6e,#1d2733)"><span class="go"><svg width="14" height="12" viewBox="0 0 14 12"><path d="M1 6h11M8 2l4 4-4 4" fill="none" stroke="#fff" stroke-width="2"/></svg></span></div>
        <div class="body"><h4>Excepteur sint occaecat</h4><div class="meta"><span>Admin</span><span>2nd Nov,2018</span></div><p>Nemo enim ipsam voluptatem quia voluptas sit aspernatur.</p></div>
      </article>
      <article class="card">
        <div class="photo" role="img" aria-label="Worker in protective suit treating a wall" style="background:linear-gradient(135deg,#d9d6cf,#a9a49a)"><span class="go"><svg width="14" height="12" viewBox="0 0 14 12"><path d="M1 6h11M8 2l4 4-4 4" fill="none" stroke="#fff" stroke-width="2"/></svg></span></div>
        <div class="body"><h4>Ducimus qui blanditis</h4><div class="meta"><span>Admin</span><span>3rd Nov,2018</span></div><p>Reiciendis voluptatibus maiores alias consequatur aut perferendis.</p></div>
      </article>
      <article class="card">
        <div class="photo" role="img" aria-label="Hand sketching architectural plans" style="background:linear-gradient(135deg,#f1f1f1,#c9cdd2)"><span class="go"><svg width="14" height="12" viewBox="0 0 14 12"><path d="M1 6h11M8 2l4 4-4 4" fill="none" stroke="#fff" stroke-width="2"/></svg></span></div>
        <div class="body"><h4>Eligendi optio cumque</h4><div class="meta"><span>Admin</span><span>23rd Oct,2018</span></div><p>Temporibus autem quibusdam et aut officiis debitis aut rerum sint.</p></div>
      </article>
    </div>
  </div>
</section>

<section class="clients">
  <div class="wrap"><span>Morvane Estates</span><span>Calvetra</span><span>Tressly</span><span>Pindora</span></div>
</section>

<footer>
  <div class="footer">
    <div class="wrap">
      <div class="col">
        <h4>Contact Us</h4>
        <ul class="contact-list">
          <li><svg width="12" height="16" viewBox="0 0 12 16"><path d="M6 0a6 6 0 0 0-6 6c0 4 6 10 6 10s6-6 6-10a6 6 0 0 0-6-6zm0 8a2 2 0 1 1 0-4 2 2 0 0 1 0 4z" fill="#ddd"/></svg>116, eius modi tempora incidunt ut<br>labore et dolore magnam</li>
          <li><svg width="14" height="14" viewBox="0 0 14 14"><path d="M3 0l3 3-2 2c1 2 3 4 5 5l2-2 3 3-2 3C6 14 0 8 0 3z" fill="#ddd"/></svg>000 - 0000 - 0000</li>
          <li><svg width="14" height="10" viewBox="0 0 14 10"><rect width="14" height="10" fill="#ddd"/><path d="M0 0l7 6 7-6" fill="none" stroke="#2b2b2b" stroke-width="1.5"/></svg>info@n4c.com</li>
        </ul>
        <div class="social"><span></span><span></span><span></span><span></span></div>
      </div>
      <div class="col">
        <h4>Quick Contact</h4>
        <div class="field">Name...</div>
        <div class="field">Email...</div>
        <div class="field area">Message...</div>
        <span class="btn">Submit</span>
      </div>
      <div class="col">
        <h4>Newsletter</h4>
        <p style="margin-bottom:12px">Subscribe to our newsletter for latest updates</p>
        <div class="field">Email...</div>
        <span class="btn">Subscribe</span>
      </div>
    </div>
  </div>
  <div class="bottombar"><div class="wrap">©Copyright Information Here</div></div>
</footer>

</body>
</html>
```